Wordpress theme for new e-commerce tropical furniture manufacturing business

We want to develop a Wordpress theme to suit our new Reefline Furniture website currently under development, business details as below.
Please see attached logo design for ideas of the design. This logo will be used as - letterhead, business cards, furniture labels etc.
We are a small Australian family business that provides products as below:
- Hand Crafted, Creative Tropical design Furniture,
(manufacture and sales).
- Specializing in mirror- wall art
- One off – designs 'made to order'.
- Individually badged pieces, each with an identification production number.
Materials used that may be incorporated in the 'web theme designs' are: Bamboo, Wood, Waves, Ocean, Shells, Tropical flowers (eg; Hibiscus, Frangipani, Heliconias, Stralitzias), Palms,Pandanus & Stone etc. etc.
Industry/Entity Type
E-Commerce
Colors
Designer to choose colors to be used in the design.
Look and feel
Each slider illustrates characteristics of the customer's brand and the style your logo design should communicate.

```html
<!DOCTYPE html>
<html lang="en">
<head>
<meta charset="utf-8">
<title>Reefline Furniture – Home</title>
<link rel="stylesheet" href="https://fonts.googleapis.com/css2?family=Roboto+Condensed:wght@400;700&family=Arimo:wght@400;700&family=Caveat:wght@500&display=swap">
<style>
:root{
  --bamboo-dark:#5a3a1c;
  --bamboo-light:#b98a4a;
  --wood:#4b2e1b;
  --wood-light:#6b452a;
  --sand:#e6bc83;
  --earth:#8b6634;
  --earth-text:#8a6433;
  --ribbon-text:#f3d7a6;
  --slate:#3e4649;
  --paper:#f4f1ea;
  --gold:#e8c48a;
  --white:#ffffff;
  --ink:#1f1a14;
  --sea:#2f7fb6;
  --sea-light:#8cc6e6;
}
*{box-sizing:border-box;margin:0;padding:0}
html,body{width:1086px;height:1200px;overflow:hidden}
body{font-family:"Arimo",Arial,sans-serif;color:var(--ink);position:relative;
  background:linear-gradient(90deg,var(--bamboo-dark) 0%,var(--bamboo-light) 20%,var(--bamboo-dark) 40%,var(--bamboo-light) 60%,var(--bamboo-dark) 80%,var(--bamboo-light) 100%)}
.abs{position:absolute}
.backdrop{left:0;top:0;width:1086px;height:1200px}
.foliage{border-radius:50%}
.foliage-top-right{left:900px;top:0;width:230px;height:260px;background:radial-gradient(circle,#4e8a3a 0%,rgba(78,138,58,0) 70%)}
.foliage-left{left:-40px;top:380px;width:220px;height:420px;background:radial-gradient(ellipse,#6e8a4c 0%,#9a3a55 35%,rgba(110,138,76,0) 70%)}
.foliage-right{left:920px;top:280px;width:200px;height:420px;background:radial-gradient(ellipse,#c04a6a 0%,#6e8a4c 40%,rgba(110,138,76,0) 70%)}
.foliage-top-left{left:60px;top:70px;width:160px;height:200px;background:radial-gradient(circle,#5d9440 0%,rgba(93,148,64,0) 70%)}
.blossoms{left:790px;top:1000px;width:330px;height:240px;background:radial-gradient(ellipse,#fff6d6 0%,#f3c94a 35%,rgba(243,201,74,0) 70%)}
.seashell{left:-20px;top:1060px;width:170px;height:170px;background:radial-gradient(circle,#e79a82 0%,#c8664f 45%,rgba(200,102,79,0) 72%)}

.topbar{left:156px;top:0;width:774px;height:84px;background:linear-gradient(180deg,var(--wood-light),var(--wood));box-shadow:0 4px 8px rgba(0,0,0,.45)}
.call{left:22px;top:17px;display:flex;align-items:center;gap:8px;color:var(--gold);font-family:"Roboto Condensed",sans-serif;font-size:14px}
.account-links{right:26px;top:18px;display:flex;gap:14px;color:var(--gold);font-family:"Roboto Condensed",sans-serif;font-size:9px;text-transform:uppercase}
.main-nav{left:0;top:52px;width:774px;font-family:"Roboto Condensed",sans-serif;font-weight:700;font-size:14px;color:var(--white)}
.main-nav span{position:absolute;top:0}

.hero{left:160px;top:104px;width:820px;height:296px;background:#cfc6b2;border-radius:6px;transform:rotate(-.6deg);box-shadow:0 6px 10px rgba(0,0,0,.35)}
.hero-photo{left:12px;top:16px;width:796px;height:268px;background:linear-gradient(180deg,var(--sea-light) 0%,var(--sea) 45%,#3b3326 70%,#d9a73c 100%)}
.tagline{left:46px;top:206px;font-family:"Caveat",cursive;font-size:32px;color:var(--white)}
.dots{left:738px;top:246px;display:flex;gap:3px}
.dots i{width:7px;height:7px;border-radius:50%;background:rgba(255,255,255,.6)}
.dots i:first-child{background:var(--white)}

.sign-strings{left:160px;top:50px;width:280px;height:120px}
.sign{left:152px;top:144px;width:272px;height:160px;background:#c9a06a;border-radius:4px;box-shadow:0 4px 8px rgba(0,0,0,.4)}
.sign-card{left:8px;top:6px;width:256px;height:142px;background:var(--white);display:flex;flex-direction:column;align-items:center;justify-content:center;gap:10px}
.brand{font-family:"Roboto Condensed",sans-serif;font-weight:700;color:var(--sea);font-size:25px;display:flex;align-items:center;gap:8px}
.brand .mark{width:12px;height:12px;border-radius:50%;background:var(--sea)}
.sign-url{font-size:9px;color:#555;letter-spacing:.5px}

.panel{left:156px;top:392px;width:774px;height:724px;background:var(--white)}
.panel-inner{left:8px;top:0;width:758px;height:716px;background:var(--sand)}

.logo-oval{left:300px;top:440px;width:252px;height:84px;border-radius:50%;background:var(--white);display:flex;align-items:center;justify-content:center;box-shadow:0 3px 5px rgba(0,0,0,.2)}
.logo-oval .brand{font-size:22px}
.intro{left:176px;top:550px;width:500px;text-align:center;font-size:11px;line-height:19px}

.ribbon{left:328px;top:604px;width:192px;height:60px}
.ribbon-label{left:328px;top:620px;width:192px;text-align:center;font-family:"Roboto Condensed",sans-serif;font-weight:700;font-size:16px;color:var(--ribbon-text)}

.product{width:158px;top:696px;text-align:center}
.product-photo{width:158px;height:122px;border:3px solid var(--white)}
.product h3{margin-top:14px;font-family:"Roboto Condensed",sans-serif;font-weight:700;font-size:17px;color:var(--earth-text)}
.product p{margin-top:8px;font-size:9.6px;line-height:17px}
.btn-earth{display:inline-block;margin-top:14px;width:90px;height:24px;line-height:24px;background:var(--sand);border:2px solid var(--earth);border-radius:2px;font-family:"Roboto Condensed",sans-serif;font-weight:700;font-size:10px;color:var(--earth-text);box-shadow:2px 2px 0 var(--earth)}

.sidebar{left:721px;top:430px;width:197px;height:555px;background:var(--slate)}
.polaroid{background:var(--paper);box-shadow:2px 3px 6px rgba(0,0,0,.5)}
.about-card{left:19px;top:14px;width:162px;height:174px}
.about-photo{left:8px;top:10px;width:144px;height:112px;background:linear-gradient(180deg,#7cc3ea 0%,#2d8fc4 45%,#efe2c2 75%)}
.about-card h3{position:absolute;left:0;top:132px;width:100%;text-align:center;font-family:"Roboto Condensed",sans-serif;font-weight:700;font-size:17px}
.side-text{left:10px;top:198px;width:177px;text-align:center;color:var(--white);font-size:9.6px;line-height:17px}
.btn-light{left:53px;top:294px;width:90px;height:26px;line-height:22px;border:2px solid var(--white);text-align:center;color:var(--white);font-family:"Roboto Condensed",sans-serif;font-weight:700;font-size:10px}
.gallery-card{left:15px;top:350px;width:172px;height:176px;transform:rotate(-3deg)}
.gallery-photo{left:10px;top:10px;width:146px;height:122px;background:linear-gradient(135deg,#b88a5a,#e6cfae 55%,#8c5a36)}
.gallery-card h3{position:absolute;left:0;top:146px;width:100%;text-align:center;font-family:"Roboto Condensed",sans-serif;font-weight:700;font-size:14px}

.footer{left:172px;top:1018px;width:742px;height:82px;background:var(--earth);color:var(--white)}
.footer-nav{left:27px;top:23px;display:flex;gap:0;font-family:"Roboto Condensed",sans-serif;font-size:9.6px}
.footer-nav span{position:absolute;top:0;white-space:nowrap}
.copyright{left:27px;top:45px;font-family:"Roboto Condensed",sans-serif;font-size:9.2px;white-space:nowrap}
.social{left:584px;top:24px;display:flex;gap:7px}
.social i{width:30px;height:30px;border:1.5px solid rgba(255,255,255,.75);border-radius:50%}
</style>
</head>
<body>
<div class="abs backdrop" role="img" aria-label="Background of upright bamboo poles"></div>
<div class="abs foliage foliage-top-right" role="img" aria-label="Palm fronds"></div>
<div class="abs foliage foliage-top-left" role="img" aria-label="Palm fronds"></div>
<div class="abs foliage foliage-left" role="img" aria-label="Tropical leaves and pink flowers"></div>
<div class="abs foliage foliage-right" role="img" aria-label="Frangipani and pink tropical flowers"></div>
<div class="abs foliage blossoms" role="img" aria-label="Cluster of frangipani blossoms"></div>
<div class="abs foliage seashell" role="img" aria-label="Scallop seashell"></div>

<header class="abs topbar">
  <div class="abs call">
    <svg width="24" height="24" viewBox="0 0 24 24" aria-hidden="true"><circle cx="12" cy="12" r="11" fill="none" stroke="#e8c48a" stroke-width="1.3"/><path d="M8 6.5c1-.6 1.6 0 2 1l.6 1.4c.3.7 0 1.2-.6 1.6.6 1.5 1.6 2.6 3 3.3.4-.6 1-.9 1.7-.6l1.4.6c1 .4 1.3 1.2.6 2-1 1.2-2.3 1.3-3.8.6-2.5-1.2-4.4-3.2-5.4-5.7-.6-1.6-.6-3.2.5-4.2z" fill="#e8c48a"/></svg>
    CALL US : ( 1300 ) 555 019
  </div>
  <div class="abs account-links"><span>My Account</span><span>|</span><span>My Cart</span><span>|</span><span>Your Cart is : 0 Items</span></div>
  <nav class="abs main-nav">
    <span style="left:165px">HOME</span>
    <span style="left:265px">ABOUT US</span>
    <span style="left:393px">PRODUCTS</span>
    <span style="left:525px">SERVICES</span>
    <span style="left:649px">CONTACT US</span>
  </nav>
</header>

<section class="abs hero">
  <div class="abs hero-photo" role="img" aria-label="Overwater bungalows on a boardwalk lit at dusk over a calm blue sea"></div>
  <div class="abs tagline">We are a small Australian family business</div>
  <div class="abs dots"><i></i><i></i><i></i><i></i></div>
</section>

<svg class="abs sign-strings" viewBox="0 0 280 120" aria-hidden="true">
  <line x1="127" y1="10" x2="9" y2="109" stroke="#5a4a3a" stroke-width="1.5"/>
  <line x1="127" y1="10" x2="245" y2="109" stroke="#5a4a3a" stroke-width="1.5"/>
  <circle cx="127" cy="10" r="8" fill="#ddd" stroke="#777"/>
</svg>
<div class="abs sign">
  <div class="abs sign-card">
    <div class="brand"><span class="mark"></span>Reefline Furniture</div>
    <div class="sign-url">www.reeflinefurniture.com.au</div>
  </div>
</div>

<main class="abs panel"><div class="abs panel-inner"></div></main>

<div class="abs logo-oval"><div class="brand"><span class="mark"></span>Reefline Furniture</div></div>
<p class="abs intro">Many desktop publishing packages and web page editors now use Lorem Ipsum as their default model text, and a search for 'lorem ipsum' will uncover many web sites still in their infancy.</p>

<svg class="abs ribbon" viewBox="0 0 192 60" aria-hidden="true">
  <polygon points="14,24 34,22 34,54 0,60 12,44" fill="#7a5428"/>
  <polygon points="176,0 192,0 184,16 188,32 168,34 168,8" fill="#7a5428"/>
  <polygon points="28,14 172,8 166,40 34,46" fill="#8b6634"/>
</svg>
<div class="abs ribbon-label">PRODUCTS</div>

<article class="abs product" style="left:184px">
  <div class="product-photo" role="img" aria-label="Beach umbrella and wooden chairs on a white sand beach" style="background:linear-gradient(180deg,#4fb3e6,#2ab7c9 50%,#f2ecd8 70%)"></div>
  <h3>HAND CRAFTED</h3>
  <p>Many desktop publishing packages and web page editors now use Lorem Ipsum as their default model text, and a search...</p>
  <span class="btn-earth">READ MORE</span>
</article>
<article class="abs product" style="left:365px">
  <div class="product-photo" role="img" aria-label="Pink and yellow frangipani flower among green leaves" style="background:radial-gradient(circle at 55% 60%,#f3c9a0 0%,#d9536d 22%,#2f5e24 55%,#1c3a16 100%)"></div>
  <h3>TROPICAL</h3>
  <p>Many desktop publishing packages and web page editors now use Lorem Ipsum as their default model text, and a search...</p>
  <span class="btn-earth">READ MORE</span>
</article>
<article class="abs product" style="left:543px">
  <div class="product-photo" role="img" aria-label="Two pale seashells on brown sand" style="background:radial-gradient(circle at 40% 45%,#eadcc6 0%,#c8ae8c 35%,#6e4e3a 80%)"></div>
  <h3>SHELLS</h3>
  <p>Many desktop publishing packages and web page editors now use Lorem Ipsum as their default model text, and a search...</p>
  <span class="btn-earth">READ MORE</span>
</article>

<aside class="abs sidebar">
  <div class="abs polaroid about-card">
    <div class="abs about-photo" role="img" aria-label="Yellow umbrella and striped deck chairs on a beach"></div>
    <h3>ABOUT US</h3>
  </div>
  <p class="abs side-text">Many desktop publishing packages and web page editors now use Lorem Ipsum as their default model text, and a search for 'lorem ipsum' will uncover many...</p>
  <div class="abs btn-light">READ MORE</div>
  <div class="abs polaroid gallery-card">
    <div class="abs gallery-photo" role="img" aria-label="Assorted seashells on sand"></div>
    <h3>PHOTO GALLERY</h3>
  </div>
</aside>

<footer class="abs footer">
  <nav class="abs footer-nav">
    <span style="left:0">HOME</span>
    <span style="left:55px">ABOUT US</span>
    <span style="left:128px">PRODUCTS</span>
    <span style="left:203px">SERVICES</span>
    <span style="left:274px">CONTACT US</span>
  </nav>
  <div class="abs copyright">COPYRIGHT © REEFLINE FURNITURE 2014. ALL RIGHTS RESERVED.</div>
  <div class="abs social" aria-label="Social links"><i></i><i></i><i></i><i></i></div>
</footer>
</body>
</html>
```